Tellwick Asset Management - Corporate Letter Head Project

Looking for a classy design based on our current logo. Please find current logo source file in files. With our color scheme.

Target Market(s)

We're an investment firm, the letterhead needs to look professional and attractive to clients.

Industry/Entity Type

Hedgefund

Colors
0054AA
0677BA
7BADD7
CADEEF
E8F1F8

Requirements
Must have
• Our logo, address, phone number, and email

```html
<!DOCTYPE html>
<html lang="en">
<head>
<meta charset="UTF-8">
<title>Tellwick Asset Management – Letterhead</title>
<link href="https://fonts.googleapis.com/css2?family=Libre+Baskerville&family=Montserrat:wght@400;500;600&display=swap" rel="stylesheet">
<style>
  :root {
    --navy: #2d4468;
    --sky: #7badd7;
    --mist: #cadeef;
    --ice: #e8f1f8;
    --ink: #3a3d44;
    --backdrop: #dedfe1;
    --paper: #ffffff;
  }
  * { margin: 0; padding: 0; box-sizing: border-box; }
  html, body { width: 1200px; height: 1200px; overflow: hidden; }
  body {
    background: var(--backdrop);
    display: flex; align-items: center; justify-content: center;
  }
  .letterhead {
    position: relative;
    width: 792px; height: 1120px;
    background: var(--paper);
    overflow: hidden;
    box-shadow: 0 6px 24px rgba(0,0,0,0.08);
  }
  .bar { position: absolute; }
  .bar--top-light {
    left: 40px; top: 64px; width: 350px; height: 12px;
    background: var(--sky);
    clip-path: polygon(0 0, 97% 0, 100% 100%, 0 100%);
  }
  .bar--top-navy {
    left: 400px; top: 52px; width: 352px; height: 14px;
    background: var(--navy);
    clip-path: polygon(0 0, 100% 0, 100% 100%, 3% 100%);
  }
  .brand {
    position: absolute; left: 92px; top: 106px;
    display: flex; align-items: center; gap: 14px;
  }
  .brand__square {
    width: 52px; height: 52px;
    border: 2px solid var(--navy);
  }
  .brand__name {
    font-family: "Libre Baskerville", serif;
    color: var(--navy);
    font-weight: 400;
    text-transform: uppercase;
    line-height: 1;
  }
  .brand__name span { display: block; }
  .brand__name .brand__line1 { font-size: 25px; letter-spacing: 0.5px; }
  .brand__name .brand__line2 { font-size: 12px; letter-spacing: 9.4px; margin-top: 5px; }
  .rule { position: absolute; height: 2px; }
  .rule--logo { left: 92px; top: 182px; width: 370px; background: var(--navy); }
  .rule--address { left: 470px; top: 156px; width: 282px; background: var(--sky); }
  .address {
    position: absolute; left: 452px; top: 86px;
    font-family: "Libre Baskerville", serif;
    font-size: 13px; line-height: 1.25;
    letter-spacing: 0.8px;
    color: var(--navy);
    text-transform: uppercase;
  }
  .letter {
    position: absolute; left: 92px; top: 262px; width: 610px;
    font-family: "Montserrat", sans-serif;
    color: var(--ink);
    text-transform: uppercase;
  }
  .letter__salutation { font-size: 11.5px; font-weight: 600; letter-spacing: 1.2px; margin-bottom: 40px; }
  .letter__body p {
    font-size: 10px; font-weight: 500; line-height: 1.72;
    letter-spacing: 1px; margin-bottom: 17px;
  }
  .signature {
    position: absolute; left: 100px; top: 860px;
  }
  .signature__mark {
    width: 96px; height: 44px;
    background: linear-gradient(90deg, rgba(58,61,68,0.08), rgba(58,61,68,0.18), rgba(58,61,68,0.05));
    border-radius: 22px;
  }
  .signature__label {
    margin-top: 12px;
    font-family: "Montserrat", sans-serif;
    font-size: 11px; font-weight: 600; letter-spacing: 2.6px;
    color: var(--ink);
  }
  .decoration {
    position: absolute; right: 0; top: 640px;
    width: 300px; height: 420px;
    background: radial-gradient(ellipse at 70% 60%, var(--ice) 0%, rgba(232,241,248,0) 70%);
  }
  .bar--foot-light {
    right: 0; top: 992px; width: 260px; height: 14px;
    background: var(--sky);
    clip-path: polygon(4% 0, 100% 0, 100% 100%, 0 100%);
  }
  .contact-band {
    position: absolute; left: 40px; top: 1016px;
    width: 474px; height: 58px;
    background: var(--navy);
    clip-path: polygon(0 0, 95% 0, 100% 100%, 0 100%);
    display: flex; align-items: center; gap: 34px;
    padding-left: 28px;
    font-family: "Libre Baskerville", serif;
    font-size: 14px; color: #ffffff;
  }
  .contact-item { display: flex; align-items: center; gap: 10px; }
  .contact-item svg { width: 18px; height: 18px; fill: none; stroke: #ffffff; stroke-width: 1.4; }
  .bar--foot-under {
    left: 40px; top: 1082px; width: 500px; height: 20px;
    background: var(--navy); opacity: 0.9;
  }
</style>
</head>
<body>
  <main class="letterhead">
    <div class="bar bar--top-light"></div>
    <div class="bar bar--top-navy"></div>

    <div class="brand">
      <div class="brand__square"></div>
      <div class="brand__name">
        <span class="brand__line1">Tellwick Asset</span>
        <span class="brand__line2">Management</span>
      </div>
    </div>
    <div class="rule rule--logo"></div>

    <address class="address" style="font-style:normal">
      Address: Unit 7, 14 Marlow Ave,<br>
      Kenridge, Johannesburg<br>
      Gauteng, 2145
    </address>
    <div class="rule rule--address"></div>

    <section class="letter">
      <p class="letter__salutation">Dear Sir,</p>
      <div class="letter__body">
        <p>Lorem ipsum dolor sit amet, consectetuer adipiscing elit, sed diam nonummy nibh euismod tincidunt ut laoreet dolore magna aliquam erat volutpat. Ut wisi enim ad minim veniam, quis nostrud exerci tation ullamcorper suscipit lobortis nisl ut aliquip ex ea commodo consequat. Duis autem vel eum iriure dolor in hendrerit in vulputate velit esse molestie consequat, vel illum dolore eu feugiat nulla facilisis at vero eros et accumsan et iusto odio dignissim qui blandit praesent luptatum zzril delenit augue duis dolore te feugait nulla facilisi.</p>
        <p>Lorem ipsum dolor sit amet, cons ectetuer adipiscing elit, sed diam nonummy nibh euismod tincidunt ut laoreet dolore magna aliquam erat volutpat. Ut wisi enim ad minim veniam, quis nostrud exerci tation ullamcorper suscipit lobortis nisl ut aliquip ex ea commodo consequat.</p>
        <p>Lorem ipsum dolor sit amet, consectetuer adipiscing elit, sed diam nonummy nibh euismod tincidunt ut laoreet dolore magna aliquam erat volutpat. Ut wisi enim ad minim veniam, quis nostrud exerci tation ullamcorper suscipit lobortis nisl ut aliquip ex ea commodo consequat. Duis autem vel eum iriure dolor in hendrerit in vulputate velit esse molestie consequat, vel illum dolore eu feugiat nulla facilisis at vero eros et accumsan et iusto odio dignissim qui blandit praesent luptatum zzril delenit augue duis dolore te feugait nulla facilisi. Lorem ipsum dolor sit amet, cons ectetuer adipiscing elit, sed diam nonummy nibh euis-</p>
      </div>
    </section>

    <div class="signature">
      <div class="signature__mark" role="img" aria-label="Handwritten signature"></div>
      <p class="signature__label">SIGNATURE</p>
    </div>

    <div class="decoration" role="img" aria-label="Faint pale blue constellation decoration"></div>

    <div class="bar bar--foot-light"></div>
    <div class="bar bar--foot-under"></div>
    <footer class="contact-band">
      <span class="contact-item">
        <svg viewBox="0 0 24 24" aria-hidden="true"><path d="M5 3h4l2 5-2.5 1.5a11 11 0 0 0 6 6L16 13l5 2v4a2 2 0 0 1-2 2A16 16 0 0 1 3 5a2 2 0 0 1 2-2z"/></svg>
        +27 071 555 0193
      </span>
      <span class="contact-item">
        <svg viewBox="0 0 24 24" aria-hidden="true"><rect x="3" y="5" width="18" height="14" rx="1"/><path d="M3 6l9 7 9-7"/></svg>
        info@tellwick-am.co.za
      </span>
    </footer>
  </main>
</body>
</html>
```